依頼詳細
店舗は車通りの多い道路の交差点に面しております※添付ファイル参照
歩行者よりも車から見られることが圧倒的に多いのでパッと見で花屋であることがわかるようなデザインを希望しております
写真では壁面が凹凸しているのが分かると思いますが赤く囲ったところに平らなプレートを貼り付け、そこにデザインされたものを出力します、既存のロゴ等は全て取り外します※添付ファイル参照
記載項目
看板には 花 の一文字を入れて下さい、店名は必要ありません
看板サイズ:横 210cm×縦 680cm
希望イメージ
シンプル 複雑
単色 カラフル
暗い 明るい
日常 高級
遊び心 厳粛
未来的 伝統的
女性的 男性的
希望する色
ピンクメイン
納品ファイル
• 高解像度JPG (.jpg)
• イラストレーター形式 (.ai)
補足説明
■ 選んだ理由

カラーがイメージにピッタリで、デザインも写真を使わずイラストで仕上がっており一つ一つの模様も大きいため全体がハッキリとしているのでインパクトもある
色・デザイン共に建物のとのフィーリングが良いと判断しました

■ 提案者全員のお礼・コメント

長期間において多数のご提案ありがとうございました、こんなに多くのエントリーをいただけるとは思っていなかったので正直ビックリしております、おかげで当選作品を選ぶのに一週間もかかってしまいました、こちらとしてはうれしい限りです。
ただ今回当選させられなかった方々には申し訳なく思います、また次の機会ありましたらなにとぞよろしくお願いします。

```html
<!DOCTYPE html>
<html lang="ja">
<head>
<meta charset="utf-8">
<title>花 FLOWER 看板</title>
<link href="https://fonts.googleapis.com/css2?family=Zen+Antique&family=Josefin+Sans:wght@400&display=swap" rel="stylesheet">
<style>
  :root {
    --page-bg: #f4f2f3;
    --sign-pink: #ef5fa5;
    --sign-pink-deep: #e24d95;
    --type-white: #ffffff;
    --bloom-orange: #f6a23a;
    --bloom-red: #e8413f;
    --bloom-yellow: #f7d84a;
    --leaf-green: #6fbf4a;
  }
  html, body {
    margin: 0;
    padding: 0;
    width: 799px;
    height: 1200px;
    overflow: hidden;
    background: var(--page-bg);
  }
  .canvas {
    position: relative;
    width: 799px;
    height: 1200px;
  }
  .sign {
    position: absolute;
    left: 223px;
    top: 30px;
    width: 352px;
    height: 1140px;
    background: linear-gradient(180deg, var(--sign-pink) 0%, var(--sign-pink-deep) 100%);
    overflow: hidden;
  }
  .bloom-cluster {
    position: absolute;
    left: 0;
    width: 352px;
  }
  .bloom-cluster--top {
    top: 0;
    height: 330px;
    background:
      radial-gradient(circle at 30% 35%, var(--bloom-orange) 0 14%, transparent 30%),
      radial-gradient(circle at 72% 22%, var(--bloom-red) 0 12%, transparent 28%),
      radial-gradient(circle at 55% 60%, var(--bloom-yellow) 0 10%, transparent 26%),
      linear-gradient(180deg, #f58bb8 0%, #f27bb0 70%, rgba(239,95,165,0) 100%);
  }
  .bloom-cluster--bottom {
    bottom: 0;
    height: 320px;
    background:
      radial-gradient(circle at 25% 60%, var(--bloom-red) 0 12%, transparent 28%),
      radial-gradient(circle at 68% 45%, var(--bloom-orange) 0 14%, transparent 30%),
      radial-gradient(circle at 50% 85%, var(--leaf-green) 0 12%, transparent 30%),
      linear-gradient(0deg, #f27bb0 0%, #f27bb0 60%, rgba(226,77,149,0) 100%);
  }
  .sign-kanji {
    position: absolute;
    top: 380px;
    left: 0;
    width: 352px;
    margin: 0;
    text-align: center;
    font-family: "Zen Antique", serif;
    font-weight: 400;
    font-size: 210px;
    line-height: 230px;
    color: var(--type-white);
  }
  .sign-label {
    position: absolute;
    top: 680px;
    left: 0;
    width: 352px;
    margin: 0;
    text-align: center;
    font-family: "Josefin Sans", sans-serif;
    font-size: 24px;
    letter-spacing: 6px;
    color: var(--type-white);
  }
</style>
</head>
<body>
  <main class="canvas">
    <section class="sign">
      <div class="bloom-cluster bloom-cluster--top" role="img" aria-label="色とりどりの花のイラスト(上部)"></div>
      <h1 class="sign-kanji">花</h1>
      <p class="sign-label">FLOWER</p>
      <div class="bloom-cluster bloom-cluster--bottom" role="img" aria-label="色とりどりの花と葉のイラスト(下部)"></div>
    </section>
  </main>
</body>
</html>
```